Letterhead design - Harwick Group

We have just had our Logo created and our now wantng a letterhead design to incorporate this. Please use the same colours as in the logo, which is attached.
Please use the company details below
P O Box 86, Bleneheim 7315
Ph: 03 642 1937
dave@harwickgroup.co.nz
We would like a professional look
We need an overall letterhead design for our varied group of buisinesses which are based in NZ and overseas. We grow and develop buisinesses. Our companies began in NZ but we now have branches overseas as well. People are our greatest asset and we employ some incredible staff. Our buisinesses are scientific, innovative and growing in size and expertise with a financial base.

Target Market(s)

Professionals

Industry/Entity Type

Investment

Requirements
Must have
• Easy to read.
• Please use the same colours as in the logo
• Please use the company details below
• P O Box 86, Bleneheim 7315
• Ph: 03 642 1937
• dave@harwickgroup.co.nz

```html
<!DOCTYPE html>
<html lang="en">
<head>
<meta charset="utf-8">
<title>Harwick Group Letterhead</title>
<link href="https://fonts.googleapis.com/css2?family=Montserrat:wght@400;700&display=swap" rel="stylesheet">
<style>
  :root {
    --brand-green: #22b06c;
    --brand-grey: #5a5a5c;
    --text-grey: #4a4a4a;
    --paper: #ffffff;
    --backdrop: #e9ecea;
    --watermark: #eef2ef;
  }
  * { margin: 0; padding: 0; box-sizing: border-box; }
  html, body { width: 1200px; height: 1200px; overflow: hidden; }
  body {
    background: var(--backdrop);
    font-family: "Montserrat", sans-serif;
    position: relative;
  }
  .letterhead {
    position: absolute;
    left: 211px;
    top: 50px;
    width: 778px;
    height: 1100px;
    background: var(--paper);
    overflow: hidden;
    box-shadow: 0 4px 24px rgba(0,0,0,0.08);
  }

  .rule-top, .rule-bottom {
    position: absolute;
    left: 0;
    right: 0;
  }
  .rule-top { top: 0; height: 10px; background: var(--brand-green); }
  .rule-top::after {
    content: "";
    position: absolute;
    left: 0; right: 0; top: 10px;
    height: 3px;
    background: var(--brand-grey);
  }
  .rule-bottom { bottom: 0; height: 10px; background: var(--brand-green); }
  .rule-bottom::before {
    content: "";
    position: absolute;
    left: 0; right: 0; top: -3px;
    height: 3px;
    background: var(--brand-grey);
  }

  .brand {
    position: absolute;
    left: 60px;
    top: 52px;
    display: flex;
    align-items: center;
    gap: 14px;
  }
  .brand-square {
    width: 32px;
    height: 32px;
    background: var(--brand-green);
  }
  .brand-name {
    font-weight: 700;
    font-size: 32px;
    letter-spacing: 1px;
    color: var(--brand-green);
    text-transform: uppercase;
  }

  .watermark {
    position: absolute;
    left: 0;
    right: 0;
    top: 500px;
    text-align: center;
    font-weight: 700;
    font-size: 64px;
    letter-spacing: 2px;
    color: var(--watermark);
    text-transform: uppercase;
  }

  .contact {
    position: absolute;
    right: 60px;
    bottom: 40px;
    list-style: none;
    font-size: 14px;
    color: var(--text-grey);
    line-height: 1;
  }
  .contact li { display: flex; align-items: center; gap: 8px; margin-top: 9px; }
  .contact svg { width: 14px; height: 14px; flex: none; }
</style>
</head>
<body>
  <main class="letterhead">
    <div class="rule-top"></div>

    <header class="brand">
      <span class="brand-square"></span>
      <span class="brand-name">Harwick Group</span>
    </header>

    <div class="watermark" aria-hidden="true">Harwick Group</div>

    <ul class="contact">
      <li>
        <svg viewBox="0 0 14 14"><rect width="14" height="14" rx="3" fill="#22b06c"/><path d="M4 3.5c.6-.4 1.2 0 1.5.6l.4.9c.2.4 0 .8-.3 1l-.4.3c.4.9 1.1 1.6 2 2l.3-.4c.2-.3.6-.5 1-.3l.9.4c.6.3 1 .9.6 1.5-.5.8-1.5 1-2.4.6C5.6 9.3 4.7 8.4 3.9 6.4c-.4-.9-.2-2.1.1-2.9z" fill="#fff"/></svg>
        03 642 1937
      </li>
      <li>
        <svg viewBox="0 0 14 14"><rect width="14" height="14" rx="3" fill="#22b06c"/><rect x="3" y="4" width="8" height="6" rx="1" fill="none" stroke="#fff" stroke-width="1.2"/><path d="M3.3 4.5 7 7.4l3.7-2.9" fill="none" stroke="#fff" stroke-width="1.2"/></svg>
        dave@harwickgroup.co.nz
      </li>
      <li>
        <svg viewBox="0 0 14 14"><rect width="14" height="14" rx="3" fill="#22b06c"/><path d="M7 2.8a3 3 0 0 1 3 3c0 2.2-3 5.4-3 5.4S4 8 4 5.8a3 3 0 0 1 3-3z" fill="#fff"/><circle cx="7" cy="5.8" r="1.1" fill="#22b06c"/></svg>
        P O Box 86, Bleneheim 7315
      </li>
    </ul>

    <div class="rule-bottom"></div>
  </main>
</body>
</html>
```